Book cover design for the book titled "Quieter Under Lanterns."

create a book cover. The book title is, "Quieter Under Lanterns: A Ledger of Harbour Songs Across Mild Winters." The purpose of the book is to create awareness of how childhood trauma is impacting 7 out of 10 adults in the world today and that two-thirds of children will experience neglect and or abuse before their 18th birthday. One victim described that his mental and physical illness resulting from childhood trauma felt like he wa being pulled to the ground, that the force was "quieter under lanterns." The design should be clean and simple and communicate a crisis.

```html
<!DOCTYPE html>
<html lang="en">
<head>
<meta charset="utf-8">
<title>Quieter Under Lanterns – Book Cover</title>
<link rel="stylesheet" href="https://fonts.googleapis.com/css2?family=Poppins:wght@600;700;800&display=swap">
<style>
  :root {
    --page-bg: #000000;
    --cover-top: #d3b92e;
    --cover-bottom: #d98e2a;
    --ink: #0a0a0a;
    --paper: #ffffff;
    --highlight: #f6ee1f;
    --figure-light: #63c4f0;
    --figure-mid: #3f8fd8;
    --figure-deep: #2a4fa8;
  }
  * { box-sizing: border-box; margin: 0; padding: 0; }
  html, body {
    width: 1200px;
    height: 1200px;
    overflow: hidden;
    background: var(--page-bg);
  }
  .cover {
    position: absolute;
    left: 360px;
    top: 240px;
    width: 480px;
    height: 720px;
    overflow: hidden;
    background: linear-gradient(160deg, var(--cover-top) 0%, #d6a42c 45%, var(--cover-bottom) 100%);
    font-family: 'Poppins', sans-serif;
  }
  .title {
    position: absolute;
    left: 0;
    top: 18px;
    width: 100%;
    text-align: center;
    font-weight: 700;
    font-size: 88px;
    line-height: 104px;
    letter-spacing: -1.5px;
    white-space: nowrap;
  }
  .title-line { display: block; }
  .title-line--dark { color: var(--ink); }
  .title-line--light { color: var(--paper); }

  .figure-art {
    position: absolute;
    left: 0;
    top: 345px;
    width: 222px;
    height: 375px;
    border-radius: 0 110px 0 0;
    background:
      radial-gradient(ellipse at 30% 45%, var(--figure-light) 0%, var(--figure-mid) 45%, transparent 75%),
      linear-gradient(180deg, var(--figure-mid) 0%, var(--figure-deep) 100%);
  }

  .subtitle {
    position: absolute;
    right: 14px;
    top: 350px;
    display: flex;
    flex-direction: column;
    align-items: flex-end;
    font-weight: 700;
    font-size: 35px;
    line-height: 47px;
    text-transform: uppercase;
  }
  .subtitle-line { color: var(--paper); padding: 0 4px; }
  .subtitle-line--boxed {
    color: var(--highlight);
    background: var(--ink);
    line-height: 38px;
    margin: 4.5px 0;
  }

  .author {
    position: absolute;
    right: 26px;
    top: 660px;
    font-weight: 700;
    font-size: 29px;
    color: var(--ink);
  }
</style>
</head>
<body>
  <main class="cover">
    <h1 class="title">
      <span class="title-line title-line--dark">QUIETER</span>
      <span class="title-line title-line--light">UNDER</span>
      <span class="title-line title-line--dark">LANTERNS</span>
    </h1>

    <div class="figure-art" role="img" aria-label="Illustration of layered blue head silhouettes in profile"></div>

    <p class="subtitle">
      <span class="subtitle-line">A Ledger of</span>
      <span class="subtitle-line subtitle-line--boxed">Harbour</span>
      <span class="subtitle-line subtitle-line--boxed">Songs</span>
      <span class="subtitle-line">Across</span>
      <span class="subtitle-line subtitle-line--boxed">Mild</span>
      <span class="subtitle-line subtitle-line--boxed">Winters</span>
    </p>

    <p class="author">AUTHOR NAME</p>
  </main>
</body>
</html>
```